Poster Design Project

We are launching a new company Q Vizo, we sell advertising on digital signage and we are launching our company selling ads at our 2 locations, Barlow Heights Sports and Rec Club and the Merrowby Bay Sports and Rec Club. We want to advertise that we have 5 10 and 15 ad slots available and ads start from as little as $27.00 per week. We need to let people know we offer 10% discount to KNBTA members. it needs to have the following contact details to get more information, Marcus 0427359012 and marcus@qvizo.com.au. As a new launch we are offering for the first 10 customers one of 2 discounts, get 4 weeks free all you have to pay is the content creation fee ($99 for 5 second ad) or 4 weeks free and free content creation if you sign up to a 18 week contract.

Update: need the add to start wit something like this but you can be creative:

Need to get you message or brand out, Have you heard of digital sinage?
We have ads avaliable starting from $27 per week at one of our locations.

Or something like that, as i am introducing my company they dont know what i do you untill they read this poster.

Target Market(s)

Targeting small to medium buisness

Industry/Entity Type

Advertising

Requirements
Must have
• Logo

```html
<!DOCTYPE html>
<html lang="en">
<head>
<meta charset="utf-8">
<title>Q Vizo – Digital Signage Advertising</title>
<link rel="stylesheet" href="https://fonts.googleapis.com/css2?family=Archivo:wght@700;800;900&display=swap">
<style>
  :root {
    --bg-top: #4d5457;
    --bg-mid: #2f3335;
    --bg-bottom: #1b1c1d;
    --text: #ffffff;
    --accent-orange: #f39c12;
    --badge-blue: #4fb3e8;
    --contact-band: #0d0d0d;
    --wave-grey: #b9bcbe;
    --wave-green: #5fb52a;
  }
  * { box-sizing: border-box; margin: 0; padding: 0; }
  html, body { width: 855px; height: 1200px; overflow: hidden; }
  body { font-family: "Archivo", Arial, Helvetica, sans-serif; color: var(--text); }

  .poster {
    position: relative;
    width: 855px;
    height: 1200px;
    overflow: hidden;
    background: linear-gradient(180deg, var(--bg-top) 0%, var(--bg-mid) 40%, var(--bg-bottom) 65%, var(--bg-bottom) 100%);
  }

  .brand {
    position: absolute;
    top: 110px; left: 0; width: 100%;
    display: flex; justify-content: center; align-items: center; gap: 14px;
  }
  .brand-mark { width: 34px; height: 34px; background: var(--badge-blue); }
  .brand-name { font-weight: 900; font-size: 46px; color: var(--text); letter-spacing: 0.5px; }

  .headline {
    position: absolute;
    top: 192px; left: 0; width: 100%;
    text-align: center;
    font-weight: 900; font-size: 50px; line-height: 64px;
    letter-spacing: 0.5px;
  }

  .slots {
    position: absolute;
    top: 338px; left: 0; width: 100%;
    text-align: center;
    font-weight: 800; font-size: 21.5px; line-height: 30px;
  }

  .offers-title {
    position: absolute;
    top: 418px; left: 0; width: 855px; padding-right: 0;
    text-align: center;
    font-weight: 800; font-size: 28px; color: var(--accent-orange);
    transform: translateX(1px);
  }
  .offers-lead {
    position: absolute;
    top: 458px; left: 0; width: 836px;
    text-align: center;
    font-weight: 800; font-size: 20.5px; line-height: 30px;
  }
  .offers-detail {
    position: absolute;
    top: 529px; left: 0; width: 836px;
    text-align: center;
    font-weight: 800; font-size: 17.5px; line-height: 25px;
  }
  .locations {
    position: absolute;
    top: 638px; left: 0; width: 810px;
    text-align: center;
    font-weight: 800; font-size: 14.5px; line-height: 22px;
  }

  .member-badge {
    position: absolute;
    left: 696px; top: 388px;
    width: 124px; height: 124px; border-radius: 50%;
    background: var(--badge-blue);
    display: flex; flex-direction: column; align-items: center; justify-content: center;
    transform: rotate(18deg);
    font-weight: 800; color: var(--text); text-align: center;
  }
  .member-badge .pct { font-size: 22px; line-height: 22px; }
  .member-badge .small { font-size: 15px; line-height: 17px; }

  .wave-art {
    position: absolute;
    left: 0; top: 700px; width: 855px; height: 340px;
    background:
      radial-gradient(ellipse 380px 90px at 420px 230px, rgba(95,181,42,0.55), rgba(95,181,42,0) 70%),
      radial-gradient(ellipse 520px 120px at 330px 150px, rgba(185,188,190,0.35), rgba(185,188,190,0) 70%),
      radial-gradient(ellipse 420px 80px at 680px 120px, rgba(185,188,190,0.28), rgba(185,188,190,0) 70%),
      transparent;
  }

  .contact-band {
    position: absolute;
    left: 0; top: 1040px; width: 855px; height: 160px;
    background: var(--contact-band);
    padding-top: 18px;
    text-align: center;
    font-weight: 800; font-size: 49px; line-height: 66px;
    letter-spacing: 0.5px;
  }
</style>
</head>
<body>
  <main class="poster">
    <header class="brand">
      <span class="brand-mark" aria-hidden="true"></span>
      <span class="brand-name">Q Vizo</span>
    </header>

    <h1 class="headline">Need advertising on<br>digital signage?</h1>

    <p class="slots">We have 5, 10 and 15 ad slots available<br>starting from as little as $27.00 per week.</p>

    <h2 class="offers-title">New launch Offers</h2>
    <p class="offers-lead">Be one of our first 10 customers and<br>receive one of 2 discounts.</p>
    <p class="offers-detail">4 weeks free all you have to pay is the content creation<br>fee ($99 for 5 second ad) OR 4 weeks free and free content<br>creation if you sign up to a 18 week contract.</p>

    <p class="locations">2 locations, Barlow Heights Sports and Rec Club and<br>the Merrowby Bay Sports and Rec Club</p>

    <div class="member-badge">
      <span class="pct">10%</span>
      <span class="small">discount<br>to KNBTA<br>members</span>
    </div>

    <div class="wave-art" role="img" aria-label="Decorative flowing grey and green light ribbons"></div>

    <footer class="contact-band">
      <div class="contact-phone">Marcus 0427359012</div>
      <div class="contact-email">marcus@qvizo.com.au</div>
    </footer>
  </main>
</body>
</html>
```